BrookfieldVentures Business Card Design

Design business cards with attached ideas. I am open to several different ideas that would be interesting and innovative. What I have provided is logo and colors. Font should be Helvetica although it could be bold or light as needed. The design can be vertical or horizontal. The design should be more interesting than a standard business card. Files must be ready to send to a printer and in Illustrator format. The text with the five icons should be exact. Send me some ideas and I will get back to you right away. I need to choose a design within 3-5 days.

Target Market(s)

Business audience

Industry/Entity Type

Business

Contact Information for Business Card

Files should be ready to send to printer in illustrator format

Font styles to use
Sans Serif

Colors
3276b5

Requirements
Must have
• Use attached logo and two colors - blue / gray
• Include 5 offering icons and text on back
Nice to have
• Interesting and innovative design. Vertical or horizontal are both fine.

```html
<!DOCTYPE html>
<html lang="en">
<head>
<meta charset="utf-8">
<title>BrookfieldVentures Business Cards</title>
<link href="https://fonts.googleapis.com/css2?family=Arimo:wght@400;700&family=Lato:wght@400;700&display=swap" rel="stylesheet">
<style>
  :root {
    --blue: #3276b5;
    --blue-deep: #1565b8;
    --blue-light: #2a93d8;
    --gray-dark: #2d2e30;
    --gray-darker: #1f2022;
    --gray-mid: #6d6f72;
    --ink: #1d1d1f;
    --paper: #ffffff;
    --paper-shade: #eef0f3;
    --backdrop: #e9e6e1;
  }
  * { box-sizing: border-box; margin: 0; padding: 0; }
  html, body { width: 1200px; height: 786px; overflow: hidden; }
  body {
    background: var(--backdrop);
    font-family: "Arimo", Helvetica, Arial, sans-serif;
    position: relative;
  }
  .card {
    position: absolute;
    width: 525px;
    height: 300px;
    background: var(--paper);
    box-shadow: 0 10px 28px rgba(0,0,0,.18);
    overflow: hidden;
  }

  /* ---------- back: offerings ---------- */
  .card-back {
    left: 60px; top: 90px;
    background: linear-gradient(160deg, var(--paper) 0%, var(--paper-shade) 100%);
    border-top: 4px solid var(--blue-light);
  }
  .card-back::after {
    content: "";
    position: absolute; left: 0; right: 0; bottom: 0;
    height: 14px;
    background: linear-gradient(90deg, var(--blue-deep), var(--blue-light));
  }
  .offerings-title {
    position: absolute; left: 40px; top: 30px;
    font-size: 24px; font-weight: 400;
    color: var(--blue);
  }
  .offerings-list { position: absolute; left: 40px; top: 76px; list-style: none; }
  .offering {
    display: flex; align-items: center;
    height: 38px; margin-bottom: 3px;
    font-size: 14px; color: var(--ink);
  }
  .offering-icon {
    width: 34px; height: 34px; margin-right: 14px; flex: none; display: block;
  }
  .offering strong { font-weight: 700; margin-right: 4px; }

  /* ---------- front: contact ---------- */
  .card-front { left: 615px; top: 400px; }
  .brand {
    position: absolute; right: 28px; top: 44px;
  }
  .brand-row { display: flex; align-items: center; }
  .brand-mark {
    width: 28px; height: 28px; background: var(--blue); margin-right: 10px; flex: none;
  }
  .brand-name { font-size: 24px; font-weight: 700; color: var(--blue); }
  .brand-tagline {
    font-size: 11px; color: var(--gray-mid);
    margin: 4px 0 0 38px;
  }
  .name-band {
    position: absolute; left: 0; top: 112px;
    width: 290px; height: 68px;
    background: linear-gradient(90deg, var(--blue-deep), var(--blue-light));
    clip-path: polygon(0 0, 100% 0, 88% 100%, 0 100%);
    padding: 12px 0 0 26px;
    color: var(--paper);
    font-family: "Lato", Helvetica, Arial, sans-serif;
  }
  .person-name { font-size: 22px; font-weight: 400; letter-spacing: .3px; line-height: 1.1; }
  .person-role { font-size: 14px; font-weight: 400; margin-top: 4px; }
  .contact-band {
    position: absolute; left: 0; right: 0; top: 180px;
    height: 72px;
    background: linear-gradient(180deg, var(--gray-dark), var(--gray-darker));
    color: var(--paper);
    font-size: 13px;
  }
  .contact-item { position: absolute; display: flex; align-items: center; line-height: 18px; }
  .contact-item svg { width: 18px; height: 18px; margin-right: 8px; flex: none; }
  .contact-phone { left: 26px; top: 13px; }
  .contact-web { left: 26px; top: 41px; }
  .contact-email { right: 28px; top: 13px; }
</style>
</head>
<body>

<section class="card card-back" aria-label="Card back: offerings">
  <h2 class="offerings-title">BrookfieldVentures Offerings</h2>
  <ul class="offerings-list">
    <li class="offering">
      <svg class="offering-icon" viewBox="0 0 34 34" aria-hidden="true"><circle cx="17" cy="17" r="17" fill="#3276b5"/><rect x="11" y="9" width="12" height="16" rx="1" fill="#fff"/><path d="M13.5 13h7M13.5 16h7M13.5 19h7M13.5 22h4" stroke="#3276b5" stroke-width="1.2"/></svg>
      <span><strong>Concepts:</strong> Thought leadership white papers</span>
    </li>
    <li class="offering">
      <svg class="offering-icon" viewBox="0 0 34 34" aria-hidden="true"><circle cx="17" cy="17" r="17" fill="#3276b5"/><path d="M8 11c3-1 6-1 9 1v12c-3-2-6-2-9-1z M26 11c-3-1-6-1-9 1v12c3-2 6-2 9-1z" fill="#fff"/></svg>
      <span><strong>Curriculum:</strong> Short courses on strategy</span>
    </li>
    <li class="offering">
      <svg class="offering-icon" viewBox="0 0 34 34" aria-hidden="true"><circle cx="17" cy="17" r="17" fill="#3276b5"/><rect x="8" y="10" width="12" height="8" rx="2" fill="#fff"/><path d="M11 18l-1 3 4-3z" fill="#fff"/><rect x="15" y="15" width="11" height="8" rx="2" fill="#fff" stroke="#3276b5" stroke-width="1"/><path d="M23 23l1 3-4-3z" fill="#fff"/></svg>
      <span><strong>Coaching:</strong> Building your strategic leadership</span>
    </li>
    <li class="offering">
      <svg class="offering-icon" viewBox="0 0 34 34" aria-hidden="true"><circle cx="17" cy="17" r="17" fill="#3276b5"/><circle cx="17" cy="17" r="7" fill="none" stroke="#fff" stroke-width="1.6"/><circle cx="17" cy="10" r="2.2" fill="#fff"/><circle cx="11" cy="21" r="2.2" fill="#fff"/><circle cx="23" cy="21" r="2.2" fill="#fff"/></svg>
      <span><strong>Consulting:</strong> Developing your strategic future</span>
    </li>
    <li class="offering">
      <svg class="offering-icon" viewBox="0 0 34 34" aria-hidden="true"><circle cx="17" cy="17" r="17" fill="#3276b5"/><rect x="8" y="9" width="18" height="13" fill="#fff"/><path d="M10.5 19l4-4 3 2.5 6-5.5" fill="none" stroke="#3276b5" stroke-width="1.4"/><path d="M17 22v4M13 26h8" stroke="#fff" stroke-width="1.6"/></svg>
      <span><strong>ScoreCard:</strong> Balanced ScoreCard and software</span>
    </li>
  </ul>
</section>

<section class="card card-front" aria-label="Card front: contact">
  <div class="brand">
    <div class="brand-row">
      <span class="brand-mark"></span>
      <span class="brand-name">BrookfieldVentures</span>
    </div>
    <p class="brand-tagline">Twice the Value - Half the Cost</p>
  </div>

  <div class="name-band">
    <p class="person-name">Dana Whitlock, Ph.d</p>
    <p class="person-role">Managing Director</p>
  </div>

  <div class="contact-band">
    <div class="contact-item contact-phone">
      <svg viewBox="0 0 18 18" aria-hidden="true"><rect width="18" height="18" rx="3" fill="#3276b5"/><path d="M5 4.5c1 3.6 4.2 7.6 8.5 9l1-2-2.3-1.2-1 1c-1.6-.8-3-2.3-3.8-3.9l1-1L7 4z" fill="#fff"/></svg>
      <span>(555) 014-2237</span>
    </div>
    <div class="contact-item contact-web">
      <svg viewBox="0 0 18 18" aria-hidden="true"><rect width="18" height="18" rx="3" fill="#3276b5"/><circle cx="9" cy="9" r="5" fill="none" stroke="#fff" stroke-width="1.2"/><path d="M4 9h10M9 4c-2.4 3-2.4 7 0 10M9 4c2.4 3 2.4 7 0 10" fill="none" stroke="#fff" stroke-width="1"/></svg>
      <span>www.brookfieldventures.com</span>
    </div>
    <div class="contact-item contact-email">
      <svg viewBox="0 0 18 18" aria-hidden="true"><rect width="18" height="18" rx="3" fill="#3276b5"/><rect x="4" y="5.5" width="10" height="7" fill="#fff"/><path d="M4 5.5l5 4 5-4" fill="none" stroke="#3276b5" stroke-width="1"/></svg>
      <span>dana@brookfieldventures.com</span>
    </div>
  </div>
</section>

</body>
</html>
```